Tactical Supply Company needing memorable business card design

Our tactical supply comapny is in need of a new business card design that will set us apart from the amateurs. We sell tactical gear ranging from backpacks and range bags to apparel and other gear. We are looking for a sharp design that incorporates our logo, website, and name. Our colors are white, red, and black, or any combination of the three, preferably red and black.
I have attached our logo with our name underneath but I have also edited that design with the logo incorporated next to the name (attached).

Target Market(s)

Law enforcement, military, tactical

Industry/Entity Type

Business

Contact Information for Business Card

Include www.fernhollowprovisions-demo.com

Colors
000000
ec1f27
ffffff

Requirements
Must have
• Our name, logo, and website. This is intended to be a memorable simple card, no name, address, email, or phone number info is necessary. Designs that do include this additional info will still be considered if they are absolutely spectacular.
Should not have
• A standard template design, I can create that in my own on Cardvellum. I am looking for a new, creative design that is completely unique to my company.

```html
<!DOCTYPE html>
<html lang="en">
<head>
<meta charset="utf-8">
<title>Fernhollow Provisions – Business Card</title>
<link rel="stylesheet" href="https://fonts.googleapis.com/css2?family=Ubuntu:wght@500;700&display=swap">
<style>
  :root {
    --red: #ec1f27;
    --black: #111111;
    --white: #ffffff;
    --backdrop: #efe6d6;
    --divider: #3a3a3a;
  }
  * { margin: 0; padding: 0; box-sizing: border-box; }
  html, body {
    width: 1189px; height: 1200px; overflow: hidden;
    background: var(--backdrop);
    font-family: "Ubuntu", sans-serif;
    color: var(--black);
  }
  .card {
    position: absolute;
    left: 171px;
    width: 856px; height: 487px;
    background: var(--white);
    border-radius: 20px;
    box-shadow: 6px 8px 10px rgba(0,0,0,0.35);
    overflow: hidden;
  }
  .card--front { top: 67px; }
  .card--back { top: 627px; }

  .wordmark {
    position: absolute;
    text-align: center;
    font-weight: 700;
    color: var(--black);
    text-transform: uppercase;
    line-height: 1.05;
  }
  .card--front .wordmark {
    left: 0; right: 0; top: 150px;
    font-size: 58px;
    letter-spacing: 1px;
  }
  .card--back .wordmark {
    left: 40px; width: 334px; top: 150px;
    font-size: 38px;
  }

  .front-site {
    position: absolute;
    left: 0; right: 0; top: 394px;
    display: flex; align-items: center; justify-content: center;
    gap: 18px;
    font-size: 22px; font-weight: 700;
  }
  .front-site .rule {
    width: 102px; height: 2px; background: var(--red);
  }

  .divider {
    position: absolute; left: 410px; top: 95px;
    width: 1px; height: 245px; background: var(--divider);
  }
  .details { position: absolute; left: 453px; top: 104px; }
  .details .name { color: var(--red); font-weight: 700; font-size: 31px; line-height: 1; }
  .details .role { font-weight: 500; font-size: 21px; margin-top: 2px; }
  .details .address { font-weight: 500; font-size: 23px; line-height: 1.25; margin-top: 38px; }
  .contact { list-style: none; margin-top: 24px; }
  .contact li {
    display: flex; align-items: center; gap: 14px;
    font-weight: 500; font-size: 19px; height: 35px;
  }
  .contact svg { width: 25px; height: 25px; flex: none; }

  .wave { position: absolute; left: 0; top: 0; width: 856px; height: 487px; }
</style>
</head>
<body>

<section class="card card--front">
  <div class="wordmark">Fernhollow<br>Provisions</div>
  <div class="front-site">
    <span class="rule"></span>
    <span>www.fernhollowprovisions-demo.com</span>
    <span class="rule"></span>
  </div>
</section>

<section class="card card--back">
  <div class="wordmark">Fernhollow<br>Provisions</div>
  <div class="divider"></div>
  <div class="details">
    <p class="name">Employee Name</p>
    <p class="role">Managing Director</p>
    <p class="address">Brookvale, North Carolina<br>28990</p>
    <ul class="contact">
      <li>
        <svg viewBox="0 0 25 25" aria-hidden="true">
          <rect width="25" height="25" rx="4" fill="var(--red)"/>
          <rect x="5" y="7.5" width="15" height="10" fill="none" stroke="#fff" stroke-width="1.4"/>
          <path d="M5 7.5 L12.5 13 L20 7.5 M5 17.5 L10.5 12 M20 17.5 L14.5 12" fill="none" stroke="#fff" stroke-width="1.2"/>
        </svg>
        hello@fernhollowprovisions-demo.com
      </li>
      <li>
        <svg viewBox="0 0 25 25" aria-hidden="true">
          <rect width="25" height="25" rx="4" fill="var(--red)"/>
          <circle cx="12.5" cy="12.5" r="7" fill="none" stroke="#fff" stroke-width="1.3"/>
          <ellipse cx="12.5" cy="12.5" rx="3" ry="7" fill="none" stroke="#fff" stroke-width="1.1"/>
          <path d="M5.5 12.5 H19.5 M7 8.7 H18 M7 16.3 H18" stroke="#fff" stroke-width="1.1"/>
        </svg>
        www.fernhollowprovisions-demo.com
      </li>
    </ul>
  </div>
  <svg class="wave" viewBox="0 0 856 487" aria-hidden="true">
    <path d="M0 390 C200 470 420 472 570 432 S790 372 856 378 L856 487 L0 487 Z" fill="var(--red)"/>
    <path d="M4 374 C200 452 420 456 570 416 S770 352 845 360 C770 362 680 392 570 424 C420 466 200 462 4 378 Z" fill="var(--black)"/>
  </svg>
</section>

</body>
</html>
```